Crest of Morning Paddocks Business Cards with logo

Need a creative business card that pops. Colorful but professional. The attached logo should be included. We are a national horse racing partnership so we are in the equine business. Nothing cartoonlike or whimsical.

Target Market(s)

professionals - 40+

Contact Information for Business Card

Maren Dunleavy
Director of Operations
27 Ashbrook Lane
Middletown, MD. 21584

Phone (313) 555-0147

FX: (949) 555-0192

email: maren@cmpaddocks.example
cmpaddocks.example

Requirements
Must have
• All information above should be on the business card including the website address. Professional yet creative
Nice to have
• an attention grabbing design. not boring. exciting.
Should not have
• cartoon like - whimsical.

```html
<!DOCTYPE html>
<html lang="en">
<head>
<meta charset="utf-8">
<title>Crest of Morning Paddocks – Business Card</title>
<link href="https://fonts.googleapis.com/css2?family=Tinos&display=swap" rel="stylesheet">
<style>
  :root {
    --backdrop: #7a5236;
    --card-white: #ffffff;
    --card-dark: #1b1c1f;
    --navy: #2e3470;
    --gold: #c4962e;
    --ink: #555555;
    --rule: #8a8a8a;
  }
  * { margin: 0; padding: 0; box-sizing: border-box; }
  html, body {
    width: 1125px; height: 1200px; overflow: hidden;
    background: var(--backdrop);
    font-family: "Tinos", "Times New Roman", serif;
  }
  .card {
    position: absolute; left: 150px; width: 825px; height: 470px;
    border-radius: 26px;
    box-shadow: 0 4px 10px rgba(0,0,0,.35);
  }
  .card--front { top: 98px; background: var(--card-white); }
  .card--back { top: 632px; background: var(--card-dark); }

  .identity {
    position: absolute; right: 433px; top: 175px;
    text-align: right; line-height: 1;
  }
  .identity__name { color: var(--navy); font-size: 29px; margin-bottom: 4px; }
  .identity__title { color: var(--gold); font-size: 21px; margin-bottom: 6px; }
  .identity__address { color: var(--ink); font-size: 19px; line-height: 25px; }

  .divider {
    position: absolute; left: 415px; top: 185px;
    width: 2px; height: 102px; background: var(--rule);
  }

  .contacts {
    position: absolute; left: 442px; top: 180px;
    list-style: none; color: var(--ink); font-size: 19px;
  }
  .contacts li { display: flex; align-items: center; height: 25px; }
  .contacts svg { width: 18px; height: 18px; margin-right: 11px; fill: var(--navy); flex: none; }

  .brand {
    position: absolute; left: 50%; top: 50%;
    width: 222px; height: 222px; margin: -111px 0 0 -111px;
    border: 2px solid var(--gold); border-radius: 50%;
    display: flex; align-items: center; justify-content: center;
    text-align: center;
  }
  .brand__name {
    color: var(--gold); font-size: 21px; line-height: 28px;
    letter-spacing: 3px; text-transform: uppercase;
  }
</style>
</head>
<body>
  <section class="card card--front">
    <div class="identity">
      <p class="identity__name">Maren Dunleavy</p>
      <p class="identity__title">Director of Operations</p>
      <p class="identity__address">27 Ashbrook Lane<br>Middletown, MD. 21584</p>
    </div>
    <div class="divider"></div>
    <ul class="contacts">
      <li>
        <svg viewBox="0 0 24 24" aria-hidden="true"><path d="M6.6 10.8a15.1 15.1 0 0 0 6.6 6.6l2.2-2.2c.3-.3.7-.4 1-.2 1.1.4 2.3.6 3.6.6.6 0 1 .4 1 1V20c0 .6-.4 1-1 1A17 17 0 0 1 3 4c0-.6.4-1 1-1h3.5c.6 0 1 .4 1 1 0 1.3.2 2.5.6 3.6.1.3 0 .7-.2 1z"/></svg>
        (313) 555-0147
      </li>
      <li>
        <svg viewBox="0 0 24 24" aria-hidden="true"><path d="M7 3h10v5H7zM4 9h16a2 2 0 0 1 2 2v6h-4v4H6v-4H2v-6a2 2 0 0 1 2-2zm4 7v3h8v-3z"/></svg>
        (949) 555-0192
      </li>
      <li>
        <svg viewBox="0 0 24 24" aria-hidden="true"><path d="M3 6h18v12H3zm2 2v.4l7 4.6 7-4.6V8l-7 4.5z"/></svg>
        maren@cmpaddocks.example
      </li>
      <li>
        <svg viewBox="0 0 24 24" aria-hidden="true"><path d="M12 2a10 10 0 1 0 0 20 10 10 0 0 0 0-20zm-1 17.9A8 8 0 0 1 4.1 11l4.9 4.9v1c0 1.1.9 2 2 2zm6.9-2.5A2 2 0 0 0 16 16h-1v-3a1 1 0 0 0-1-1H8v-2h2a1 1 0 0 0 1-1V7h2a2 2 0 0 0 2-2v-.4a8 8 0 0 1 2.9 12.8z"/></svg>
        www.cmpaddocks.example
      </li>
    </ul>
  </section>

  <section class="card card--back">
    <div class="brand">
      <p class="brand__name">Crest of<br>Morning<br>Paddocks</p>
    </div>
  </section>
</body>
</html>
```